Stationary Set and Logo Update **PAYMENT GUARANTEED**

Stationery Design and Logo Update

About Us

Trindex Supply is a wholesale distributor of OEM [original brand] and compatible [generic brand] parts and supplies for use in copiers, faxes, printers, and multi-function machines. In plain English…we sell all the parts and supplies [such as toner] that make up any office equipment which outputs an image on paper.

Trindex was the 1st distributor to develop and sell a generic brand copier part in the United States. We have been in business since 1972 [nearly 40 years]. Our tagline is "The Steady Choice," as in our company was the first alternative product that copier dealers had to buying original brand copier parts. Trindex is known for offering reliable and cost-effective OEM and compatible products.

Project

We require a fresh, modern and corporate identity. Please submit a stationary package inclusive of a double-sided business card (2" x 3.5"), letterhead (8.5'x11"), and standard #10 envelope (4-1/8” x 9-1/2). You may use our current logo or preferably your take on an updated one. If an attempt is made in updating the logo #004D8E or a similar hue should be used as the primary color.

The design should be clean, simple, modern and professional and make an immediate impact.

Target Market(s)

Copier and printer dealers who lease and service imaging equipment in the United States and Latin America.

Industry/Entity Type

Business

Requirements
Must have
• Simple, clean, modern and professional. Please use #004D8E or a similar hue as the primary color. Letterhead must accommate (2) addresses. We have 2 locations.
Nice to have
• A simple, modern update to our current logo. https://assets.mailvorbo.example/fs030/5520384417702/img/418.jpg
Should not have
• More than (2) colors on logo.

```html
<!DOCTYPE html>
<html lang="en">
<head>
<meta charset="utf-8">
<title>Trindex Supply Stationery Set</title>
<link rel="stylesheet" href="https://fonts.googleapis.com/css2?family=Arimo:wght@400;700&display=swap">
<style>
  :root {
    --brand-blue: #1d4f91;
    --ink-grey: #8a8f99;
    --paper: #ffffff;
    --backdrop: #f6f7fc;
    --shadow: 0 4px 12px rgba(20, 40, 80, 0.18);
  }
  * { margin: 0; padding: 0; box-sizing: border-box; }
  html, body {
    width: 1200px; height: 1200px; overflow: hidden;
    background: var(--backdrop);
    font-family: "Arimo", Arial, sans-serif;
  }
  .canvas { position: relative; width: 1200px; height: 1200px; }

  .sheet { position: absolute; background: var(--paper); box-shadow: var(--shadow); overflow: hidden; }
  .band { position: absolute; left: 0; right: 0; bottom: 0; background: var(--brand-blue); }

  .brand-name {
    position: absolute; color: var(--brand-blue);
    font-weight: 700; font-size: 44px; letter-spacing: -1px; line-height: 1;
  }

  .address { position: absolute; font-style: normal; font-size: 9.5px; line-height: 12.5px; color: var(--ink-grey); }
  .address .office { color: var(--brand-blue); font-weight: 700; }
  .address .site { color: var(--brand-blue); }
  .address dl { display: grid; grid-template-columns: 50px auto; }
  .address dd::before { content: ":\00a0\00a0"; }

  /* letterhead */
  .letterhead { left: 44px; top: 51px; width: 849px; height: 1098px; }
  .letterhead .band { height: 24px; }
  .letterhead .brand-name { left: 76px; top: 65px; }
  .letterhead .corporate { left: 441px; top: 53px; }
  .letterhead .western { left: 643px; top: 53px; }

  /* business card front */
  .card-front { left: 603px; top: 233px; width: 350px; height: 200px; background: var(--brand-blue); }
  .card-front .brand-name { left: 24px; top: 80px; font-size: 38px; color: var(--paper); }

  /* business card back */
  .card-back { left: 603px; top: 451px; width: 350px; height: 200px; }
  .card-back .band { height: 26px; }
  .holder { position: absolute; left: 25px; top: 36px; }
  .holder-name { font-size: 12px; font-weight: 700; color: var(--brand-blue); }
  .holder-title { font-size: 9px; color: var(--ink-grey); margin-top: 1px; }
  .card-back .address { font-size: 9px; line-height: 11.5px; top: 77px; }
  .card-back .address dl { grid-template-columns: 48px auto; }
  .card-back .corporate { left: 25px; }
  .card-back .western { left: 193px; }

  /* envelope */
  .envelope { left: 200px; top: 680px; width: 951px; height: 413px; }
  .envelope .band { height: 26px; }
  .envelope .brand-name { left: 44px; top: 165px; }
  .envelope .western { left: 300px; top: 163px; }
</style>
</head>
<body>
<main class="canvas">

  <section class="sheet letterhead" aria-label="Letterhead">
    <div class="brand-name">Trindex</div>
    <address class="address corporate">
      <div class="office">Trindex Supply</div>
      <div class="site">Corporate Office</div>
      <div>2280 NW 19th Street</div>
      <div>Pompano Beach, FL 33069</div>
      <dl><dt>Toll Free</dt><dd>800.555.0142</dd><dt>Local</dt><dd>954.555.0187</dd><dt>Fax</dt><dd>954.555.0193</dd></dl>
    </address>
    <address class="address western">
      <div class="office">Trindex West</div>
      <div class="site">West Coast Fulfillment Center</div>
      <div>North Valley Industrial Park #2</div>
      <div>2417 Harlow Court</div>
      <div>Sparks, NV 89502</div>
      <dl><dt>Toll Free</dt><dd>800.555.0166</dd><dt>Fax</dt><dd>775.555.0128</dd></dl>
    </address>
    <div class="band"></div>
  </section>

  <section class="sheet card-front" aria-label="Business card front">
    <div class="brand-name">Trindex</div>
  </section>

  <section class="sheet card-back" aria-label="Business card back">
    <div class="holder">
      <div class="holder-name">Marisol Tevar</div>
      <div class="holder-title">Marketing Coordinator</div>
    </div>
    <address class="address corporate">
      <div class="office">Trindex Supply</div>
      <div class="site">Corporate Office</div>
      <div>2280 NW 19th Street</div>
      <div>Pompano Beach, FL 33069</div>
      <dl><dt>Toll Free</dt><dd>800.555.0142</dd><dt>Direct</dt><dd>954.555.0174</dd><dt>Email</dt><dd>mtevar@trindex.com</dd></dl>
    </address>
    <address class="address western">
      <div class="office">Trindex West</div>
      <div class="site">West Coast Fulfillment Center</div>
      <div>North Valley Industrial Park #2</div>
      <div>2417 Harlow Court</div>
      <div>Sparks, NV 89502</div>
    </address>
    <div class="band"></div>
  </section>

  <section class="sheet envelope" aria-label="Number 10 envelope">
    <div class="brand-name">Trindex</div>
    <address class="address western">
      <div class="office">Trindex West</div>
      <div class="site">West Coast Fulfillment Center</div>
      <div>North Valley Industrial Park #2</div>
      <div>2417 Harlow Court</div>
      <div>Sparks, NV 89502</div>
    </address>
    <div class="band"></div>
  </section>

</main>
</body>
</html>
```